Business Card Design for Pastor/Church Leadership - simple, elegant, "different"

Design a name card based on logo and color from our branding guide - see file "MBF Logo and Color".
The teal frame around the logo is not part of the logo and is a not necessary design element for the name card (as the attached PDF file may suggest).
The font suggested by branding is "Frutiger 55 Roman".
The file "not good.pdf", a sample of a name card that is NOT good.
- fonts too small to read
- the tagline on the logo "Still waters, open door" not easy to read with logo used in this design
- "MAPLE GROVE FELLOWSHIP" unnecessarily duplicated - possibly because logo too small
- not sure about the green frame, probably better to drop

Target Market(s)

broad, all people the pastor of an international church in Tokyo meets

Industry/Entity Type

Business

Contact Information for Business Card

Mattias R. Pellworth
Pastor
3-9-4 Kawaranodai, Kirinoha-ku
Tokyo 162-0418 (Church)
2-21 Ochibamachi, Kirinoha-ku
Tokyo 162-0427 (Home)
Tel: 03-5817-2963
E-mail: pastor@maplegrovefell.org
URL: http://www.maplegrovefell.org

Font styles to use
Sans Serif
Other font styles liked:
• Frutiger 55 Roman (want, not must)

Requirements
Must have
• must include logo
• must make use of the "bright turquoise color"
• Cyan = 59, Magenta = 0, Yellow=24, Black=0
• Red=3.1%, Green=91%, Blue=87.1%
• Key Info (name) must be easy to read (see notes on bad sample namecard attached)

```html
<!DOCTYPE html>
<html lang="en">
<head>
<meta charset="utf-8">
<title>Maple Grove Fellowship – Pastor Name Card</title>
<link rel="stylesheet" href="https://fonts.googleapis.com/css2?family=Arimo:wght@400;700&display=swap">
<style>
  :root {
    --teal: #5bb8bb;
    --ink: #1c1c1c;
    --card: #ffffff;
    --backdrop: #e6e8ea;
  }
  * { margin: 0; padding: 0; box-sizing: border-box; }
  html, body {
    width: 1200px; height: 902px; overflow: hidden;
    background: var(--backdrop);
    font-family: "Arimo", Arial, sans-serif;
  }
  .name-card {
    position: absolute; left: 100px; top: 165px;
    width: 1000px; height: 572px;
    background: var(--card);
    box-shadow: 0 6px 24px rgba(0,0,0,.12);
    overflow: hidden;
  }
  .name-card__arc { position: absolute; inset: 0; }
  .brand {
    position: absolute; left: 40px; top: 250px; width: 330px;
    color: var(--teal);
  }
  .brand__mark { display: flex; align-items: center; gap: 10px; }
  .brand__dot {
    width: 18px; height: 18px; border-radius: 50%; background: var(--teal);
    flex: none;
  }
  .brand__name {
    font-size: 19px; font-weight: 400; letter-spacing: 1.5px;
    white-space: nowrap;
  }
  .brand__rule {
    height: 2px; background: var(--teal); margin: 12px 0 10px;
  }
  .brand__tagline { font-size: 20px; letter-spacing: 1px; padding-left: 8px; }

  .identity {
    position: absolute; right: 70px; top: 52px; text-align: right;
  }
  .identity__name { color: var(--teal); font-size: 40px; font-weight: 700; }
  .identity__title { color: var(--ink); font-size: 26px; font-weight: 700; margin-top: 4px; }

  .contact {
    position: absolute; right: 60px; top: 205px; list-style: none;
    text-align: right; color: var(--ink); font-size: 20px; line-height: 31px;
  }
  .contact__item { display: flex; justify-content: flex-end; align-items: center; gap: 14px; }
  .contact__icon {
    width: 18px; height: 18px; background: var(--ink); border-radius: 3px;
    display: inline-flex; align-items: center; justify-content: center; flex: none;
  }

  .addresses {
    position: absolute; right: 92px; top: 355px; font-style: normal;
    text-align: right; color: var(--ink); font-size: 20px; font-weight: 700; line-height: 27px;
  }
  .addresses__block + .addresses__block { margin-top: 14px; }
</style>
</head>
<body>
  <article class="name-card">
    <svg class="name-card__arc" viewBox="0 0 1000 572" aria-hidden="true">
      <path fill="var(--teal)" d="M288 0 L312 0 C478 130 478 410 366 572 L312 572 C418 400 420 140 288 0 Z"/>
    </svg>

    <div class="brand">
      <div class="brand__mark">
        <span class="brand__dot"></span>
        <span class="brand__name">MAPLE GROVE FELLOWSHIP</span>
      </div>
      <div class="brand__rule"></div>
      <div class="brand__tagline">Still waters, open door</div>
    </div>

    <header class="identity">
      <h1 class="identity__name">Mattias R. Pellworth</h1>
      <p class="identity__title">Pastor</p>
    </header>

    <ul class="contact">
      <li class="contact__item">03-5817-2963
        <span class="contact__icon"><svg width="12" height="12" viewBox="0 0 12 12"><path fill="#fff" d="M2 1h2l1 3-1.5 1a6 6 0 0 0 3.5 3.5L8 7l3 1v2a1 1 0 0 1-1 1A9 9 0 0 1 1 2a1 1 0 0 1 1-1z"/></svg></span>
      </li>
      <li class="contact__item">pastor@maplegrovefell.org
        <span class="contact__icon"><svg width="12" height="12" viewBox="0 0 12 12"><rect x="1" y="2.5" width="10" height="7" fill="none" stroke="#fff" stroke-width="1.2"/><path d="M1 3l5 4 5-4" fill="none" stroke="#fff" stroke-width="1.2"/></svg></span>
      </li>
      <li class="contact__item">http://www.maplegrovefell.org
        <span class="contact__icon"><svg width="12" height="12" viewBox="0 0 12 12"><circle cx="6" cy="6" r="4.5" fill="none" stroke="#fff" stroke-width="1.2"/><path d="M1.5 6h9M6 1.5c-2 2.5-2 6.5 0 9M6 1.5c2 2.5 2 6.5 0 9" fill="none" stroke="#fff" stroke-width="1"/></svg></span>
      </li>
    </ul>

    <address class="addresses">
      <div class="addresses__block">3-9-4 Kawaranodai, Kirinoha-ku<br>Tokyo 162-0418 (Church)</div>
      <div class="addresses__block">2-21 Ochibamachi, Kirinoha-ku<br>Tokyo 162-0427 (Home)</div>
    </address>
  </article>
</body>
</html>
```